Webdesign für KFZ-Service-Betrieb
Zielgruppe
Wartung, Reparatur und Instandsetzung von Kraftfahrzeugen aller Marken.
Reifenhandel, Old- und Youngtimer-Service, An- und Verkauf von Fahrzeugen.
Aufgabenstellung
Firmenfarbe ist blau.
Moderner, Übersichtlicher und Transparenter Auftritt erwünscht.

```html
<!DOCTYPE html>
<html lang="de">
<head>
<meta charset="utf-8">
<title>Blauwerk KFZ – Wir über uns</title>
<link rel="stylesheet" href="https://fonts.googleapis.com/css2?family=Libre+Baskerville:wght@400;700&family=Open+Sans:wght@400;600;700&display=swap">
<style>
  :root {
    --blue-dark: #1f2a93;
    --blue-text: #2431a3;
    --blue-light: #7f89c9;
    --white: #ffffff;
    --hero-a: #5d6f98;
    --hero-b: #2a2f3c;
    --contact-a: #3a3f4c;
    --contact-b: #20222a;
  }
  * { margin: 0; padding: 0; box-sizing: border-box; }
  html, body { width: 1200px; height: 2396px; overflow: hidden; background: var(--white); }
  body { position: relative; font-family: "Libre Baskerville", Georgia, serif; color: var(--blue-text); }

  .site-header { position: absolute; left: 0; top: 0; width: 1200px; height: 150px; }
  .brand { position: absolute; left: 41px; top: 58px; display: flex; align-items: center; gap: 12px;
    font-family: "Open Sans", Arial, sans-serif; font-weight: 600; font-size: 21px; letter-spacing: 3px;
    color: var(--blue-text); line-height: 28px; white-space: nowrap; }
  .brand-mark { width: 18px; height: 18px; background: var(--blue-text); }
  .nav-link { position: absolute; left: 494px; top: 84px; font-family: "Open Sans", Arial, sans-serif;
    font-weight: 600; font-size: 26px; letter-spacing: 5px; color: var(--blue-text); }

  .hero { position: absolute; left: 0; top: 150px; width: 1200px; height: 484px;
    background: linear-gradient(180deg, var(--hero-a) 0%, #495674 50%, var(--hero-b) 100%); }
  .hero-title { position: absolute; left: 0; top: 190px; width: 1200px; text-align: center;
    font-family: "Open Sans", Arial, sans-serif; font-weight: 600; font-size: 33px; letter-spacing: 7px;
    line-height: 59px; color: var(--white); }

  .intro { position: absolute; left: 0; top: 634px; width: 1200px; height: 246px; text-align: center; }
  .intro h1 { margin-top: 45px; font-size: 37px; font-weight: 400; letter-spacing: 1px; color: var(--blue-text); }
  .intro p { width: 1140px; margin: 6px auto 0; font-size: 17px; line-height: 23.5px; }

  .service { position: absolute; left: 0; width: 1200px; }
  .service .panel { position: absolute; top: 0; height: 100%; text-align: center; color: var(--white); }
  .service .photo { position: absolute; top: 0; height: 100%; }
  .service h2 { font-weight: 400; font-size: 39px; line-height: 51px; letter-spacing: 0.5px; }
  .service p { margin: 18px auto 0; width: 660px; font-size: 18px; line-height: 27px; }
  .btn { display: inline-block; margin-top: 38px; padding: 0 16px; height: 62px; line-height: 62px;
    background: var(--white); color: var(--blue-text); font-size: 24px; text-decoration: none; }

  .service-workshop { top: 880px; height: 382px; }
  .service-workshop .panel { left: 0; width: 748px; background: var(--blue-dark); padding-top: 48px; }
  .service-workshop .photo { left: 748px; width: 452px; background: linear-gradient(135deg, #e0b21a 0%, #3b3f7a 50%, #d8d8dc 100%); }

  .service-tyres { top: 1262px; height: 386px; }
  .service-tyres .photo { left: 0; width: 468px; background: linear-gradient(160deg, #f2f2f2 0%, #5a5a5e 55%, #2b2b2e 100%); }
  .service-tyres .panel { left: 468px; width: 732px; background: var(--blue-light); padding-top: 72px; }

  .service-trade { top: 1648px; height: 372px; }
  .service-trade .panel { left: 0; width: 743px; background: var(--blue-dark); padding-top: 36px; }
  .service-trade .photo { left: 743px; width: 457px; background: linear-gradient(180deg, #3d3d3d 0%, #b9b9b9 55%, #8a8a8a 100%); }

  .contact { position: absolute; left: 0; top: 2020px; width: 1200px; height: 376px;
    background: linear-gradient(110deg, var(--contact-b) 0%, #2f3550 45%, var(--contact-a) 100%); color: var(--white); }
  .contact h2 { position: absolute; left: 58px; top: 118px; width: 360px; text-align: center;
    font-size: 62px; line-height: 82px; font-weight: 700; }
  .hours { position: absolute; left: 460px; top: 184px; width: 280px; text-align: center;
    font-size: 15px; line-height: 27px; font-weight: 700; }
  .phone { position: absolute; left: 868px; top: 196px; display: flex; align-items: center; gap: 22px; }
  .phone svg { width: 50px; height: 50px; }
  .phone-numbers { font-size: 18px; line-height: 27px; font-weight: 700; letter-spacing: 1px; }
</style>
</head>
<body>
  <header class="site-header">
    <div class="brand"><span class="brand-mark"></span><span>BLAUWERK KFZ</span></div>
    <nav class="nav-link">Wir über uns</nav>
  </header>

  <section class="hero" role="img" aria-label="Zwei Mechaniker in blauen Overalls an einem Auto mit geöffneter Motorhaube">
    <p class="hero-title">Wartung, Reparatur und Instandsetzung<br>von Kraftfahrzeugen aller Marken.</p>
  </section>

  <section class="intro">
    <h1>PRO SOLUTIONS</h1>
    <p>loremp loremp loremp lorem lormel loremp lorem lorem lorem lorem lorem loremp loremp loremp loore lorem lorem&nbsp; lorem lorem lorem&nbsp; loremp loremp loremp loremp loremp lorem lorem loremp loremp loremp lorem lormel loremp lorem lorem lorem lorem&nbsp; lorem loremp loremp loremp loore lorem lorem&nbsp; lorem lorem lorem&nbsp; loremp loremp loremp loremp loremp lorem lorem</p>
  </section>

  <section class="service service-workshop">
    <div class="panel">
      <h2>WARTUNG, REPARATUR UND<br>INSTANDSETZUNG</h2>
      <p>loremp loremp loremp lorem lormel loremp lorem lorem lorem lorem lorem loremp loremp loremp loore lorem lorem&nbsp; lorem lorem lorem loremp loremp loremp loremp loremp lorem lorem</p>
      <a class="btn" href="#">Read more</a>
    </div>
    <div class="photo" role="img" aria-label="Mechaniker mit Kappe arbeitet im Motorraum eines weißen Autos"></div>
  </section>

  <section class="service service-tyres">
    <div class="photo" role="img" aria-label="Reihe von Autoreifen mit Alufelgen auf einer Straße"></div>
    <div class="panel">
      <h2>REIFENHANDEL</h2>
      <p>loremp loremp loremp lorem lormel loremp lorem lorem lorem lorem lorem loremp loremp loremp loore lorem lorem&nbsp; lorem lorem lorem loremp loremp loremp loremp loremp lorem lorem</p>
      <a class="btn" href="#">Read more</a>
    </div>
  </section>

  <section class="service service-trade">
    <div class="panel">
      <h2>AN- UND VERKAUF<br>VON FAHRZEUGEN</h2>
      <p>loremp loremp loremp lorem lormel loremp lorem lorem lorem lorem lorem loremp loremp loremp loore lorem lorem&nbsp; lorem lorem lorem loremp loremp loremp loremp loremp lorem lorem</p>
      <a class="btn" href="#">Read more</a>
    </div>
    <div class="photo" role="img" aria-label="Schwarzweißfoto eines klassischen Cabriolets mit Paar"></div>
  </section>

  <section class="contact" role="img" aria-label="Abgedunkeltes Foto eines Mechanikers im Kundengespräch in der Werkstatt">
    <h2>OUR<br>CONTACT</h2>
    <div class="hours">Öffnungszeiten:<br>Mo.-Fr.: 07.30 Uhr - 18.00 Uhr<br>Sa.: 09.00 Uhr-12.00 Uhr</div>
    <div class="phone">
      <svg viewBox="0 0 24 24" aria-hidden="true"><path fill="#ffffff" d="M6.6 10.8c1.4 2.8 3.8 5.1 6.6 6.6l2.2-2.2c.3-.3.7-.4 1-.2 1.1.4 2.3.6 3.6.6.6 0 1 .4 1 1V20c0 .6-.4 1-1 1C10.6 21 3 13.4 3 4c0-.6.4-1 1-1h3.5c.6 0 1 .4 1 1 0 1.3.2 2.5.6 3.6.1.3 0 .7-.2 1L6.6 10.8z"/></svg>
      <div class="phone-numbers">800-555-0147<br>800-555-0148</div>
    </div>
  </section>
</body>
</html>
```